Design a Website Mockup for Civil Engineer - Technical company

Hello to everyone,

I need a fresh and clean design for a civil engineer - technical company. It is a small company, more focused on small projects like houses and consulting services.

The design must have logo and cover section (a related photo for example) a sidebar and main content area. Each cover must be different for every page
(Home | Profile | Services | Works | Contact).

I have attached logo and colors used in their business card

Also some sample websites (just for thought)
http://www.qlo.gr/portal/
http://www.7wp.gr/
http://www.torqelan.com/

```html
<!DOCTYPE html>
<html lang="en">
<head>
<meta charset="utf-8">
<title>Stratobuild Engineers</title>
<link href="https://fonts.googleapis.com/css2?family=Open+Sans:wght@400;600;700&display=swap" rel="stylesheet">
<style>
:root{
  --orange:#f7941d;
  --blue:#1a8fd0;
  --green:#1aa98b;
  --ink:#2b2b2b;
  --text:#6b6b6b;
  --band:#f0f1f2;
  --dark:#25282c;
  --footer:#222528;
  --hero-a:#6d8fb8;
  --hero-b:#24406f;
  --white:#ffffff;
}
*{margin:0;padding:0;box-sizing:border-box}
html,body{width:1200px;height:3276px;overflow:hidden}
body{font-family:"Open Sans",Arial,sans-serif;color:var(--ink);background:var(--white);position:relative}
section,header,footer{position:absolute;left:0;width:1200px}
.abs{position:absolute}

/* header */
.site-header{top:0;height:96px;background:var(--white)}
.brand{left:110px;top:30px;display:flex;align-items:center;gap:10px;font-size:24px;font-weight:700;color:var(--ink)}
.brand-mark{width:22px;height:22px;background:var(--ink)}
.nav{left:0;top:0;height:96px;width:1200px}
.nav a{position:absolute;top:38px;font-size:14px;color:#333;text-decoration:none;transform:translateX(-50%);white-space:nowrap}
.nav a.active{color:var(--orange)}
.nav-bar{left:512px;top:91px;width:86px;height:5px;background:var(--orange)}
.flag{display:inline-block;width:16px;height:11px;background:#2d3f8f;vertical-align:-1px;margin-right:4px;border:1px solid #c8102e}

/* hero */
.hero{top:96px;height:553px;background:linear-gradient(160deg,var(--hero-a) 0%,#3d5f92 45%,var(--hero-b) 100%)}
.hero h1{left:0;width:1200px;top:147px;text-align:center;color:var(--white);font-size:34px;font-weight:400;line-height:40px;letter-spacing:1.5px}
.btn{background:var(--orange);color:var(--white);text-align:center;border-radius:3px}
.hero .btn{left:531px;top:257px;width:138px;height:38px;line-height:38px;font-size:14px}
.dots{left:565px;top:484px;display:flex;gap:6px}
.dots span{width:14px;height:14px;border:1.5px solid var(--white);border-radius:50%}
.dots span.on{background:var(--white)}

/* features */
.features{top:649px;height:412px;background:var(--band)}
.feature{top:64px;width:300px;text-align:center}
.feature .ico{margin:0 auto;width:80px;height:80px;border-radius:50%;display:flex;align-items:center;justify-content:center}
.feature h3{margin-top:28px;font-size:20px;font-weight:400}
.feature .rule{margin:12px auto 0;width:86px;height:3px}
.feature p{margin:30px auto 0;width:290px;font-size:12px;line-height:20px;color:var(--text)}
.more{display:block;margin-top:16px;font-size:11px;font-weight:700;color:var(--orange);letter-spacing:.8px}

/* about */
.about{top:1061px;height:571px}
.section-title{left:0;width:1200px;text-align:center;font-size:21px;font-weight:400}
.title-rule{left:556px;width:88px;height:3px;background:var(--orange)}
.portrait{left:163px;top:153px;width:176px;height:176px;border-radius:50%;background:linear-gradient(#e8e8e8,#9a9a9a);border:2px solid #ddd}
.person{left:110px;top:352px;width:282px;text-align:center}
.person h4{font-size:17px;font-weight:400;letter-spacing:.5px}
.person p{margin-top:14px;font-size:12px;line-height:20px;color:var(--text)}
.person em{font-style:normal;color:var(--orange)}
.svc{width:300px;height:120px}
.svc .ring{left:0;top:12px;width:74px;height:74px;border-radius:50%;border:1px solid #d8d8d8;background:var(--white);display:flex;align-items:center;justify-content:center}
.svc .ring.hot{background:var(--orange);border-color:var(--orange)}
.svc h5{left:91px;top:0;font-size:17px;font-weight:600}
.svc p{left:92px;top:31px;width:175px;font-size:10.5px;line-height:16.5px;color:var(--text)}

/* gallery */
.gallery{top:1632px;height:496px;background:var(--dark)}
.tabs{left:440px;top:27px;display:flex}
.tabs span{height:42px;line-height:42px;font-size:11px;padding:0 27px;background:var(--white);color:#333;border:1px solid #bbb}
.tabs span.on{background:#f2f2f2;color:var(--orange)}
.tile{width:300px;height:199px;display:flex;flex-direction:column;align-items:center;justify-content:center;color:var(--white)}
.tile b{font-weight:400;font-size:13px}
.tile small{margin-top:8px;font-size:9px;font-weight:600}
.tile .view{background:var(--white);color:#333;font-size:12px;padding:7px 14px;border-radius:3px}

/* news */
.news{top:2128px;height:542px}
.item{width:420px;height:133px}
.item .pic{left:0;top:0;width:200px;height:133px}
.item h6{left:220px;top:12px;font-size:14px;font-weight:400}
.item p{left:220px;top:36px;width:210px;font-size:10.5px;line-height:18px;color:var(--text)}
.item p em{font-style:normal;color:var(--orange)}
.item .date{left:220px;top:101px;font-size:10px;color:#aaa}

/* cta */
.cta{top:2670px;height:276px;background:linear-gradient(135deg,#3e5a85,#1d3560)}
.cta h2{left:0;top:67px;width:1200px;text-align:center;color:var(--white);font-size:25px;font-weight:400}
.cta .btn{left:480px;top:148px;width:240px;height:52px;line-height:52px;font-size:20px;font-weight:700}

/* footer */
.site-footer{top:2946px;height:330px;background:var(--footer);color:#cfcfcf}
.col{top:46px;width:215px}
.col h4{font-size:14px;font-weight:700;color:var(--white);letter-spacing:.8px;padding-bottom:10px;border-bottom:2px solid var(--orange)}
.col ul{list-style:none;margin-top:12px}
.col li{font-size:12px;line-height:22px}
.col p{margin-top:12px;font-size:11px;line-height:20px}
.contact-line{display:flex;gap:12px;font-size:12px;line-height:20px;margin-top:12px}
.contact-line svg{flex:none;margin-top:4px}
.field{margin-top:24px;width:218px;height:33px;background:var(--white);border-radius:3px}
.sub{margin-top:18px;width:111px;height:31px;line-height:31px;font-size:12px}
.bottom{left:0;top:276px;width:1200px;height:54px;border-top:1px solid #444;font-size:11px}
.bottom .copy{left:110px;top:20px}
.bottom .copy b{color:var(--white);font-weight:600}
.bottom .follow{left:918px;top:20px;display:flex;gap:9px;align-items:center}
.bottom .follow i{width:9px;height:9px;background:#ccc;display:block}
</style>
</head>
<body>

<header class="site-header">
  <div class="abs brand"><span class="brand-mark"></span>Stratobuild</div>
  <nav class="abs nav">
    <a class="active" style="left:557px">Home</a>
    <a style="left:646px">Profile</a>
    <a style="left:743px">Services</a>
    <a style="left:841px">Works</a>
    <a style="left:933px">Contact</a>
    <a style="left:1050px"><span class="flag"></span>English ▾</a>
  </nav>
  <div class="abs nav-bar"></div>
</header>

<section class="hero" role="img" aria-label="Photo of a glass skyscraper under construction with a tower crane against the sky">
  <h1 class="abs">Offering innovative solutions to the<br>construction industry</h1>
  <div class="abs btn">CLICK HERE</div>
  <div class="abs dots"><span></span><span></span><span class="on"></span><span></span></div>
</section>

<section class="features">
  <div class="abs feature" style="left:123px">
    <div class="ico" style="background:var(--blue)">
      <svg width="34" height="34" viewBox="0 0 34 34"><circle cx="17" cy="11" r="7" fill="#fff"/><path d="M4 32c0-8 6-12 13-12s13 4 13 12z" fill="#fff"/></svg>
    </div>
    <h3>Who we are</h3><div class="rule" style="background:var(--blue)"></div>
    <p>It is a long established fact that a reader be distracted by the readable content a page when looking at its layout. The point of using Lorem Ipsum of the round by</p>
    <span class="more">READ MORE</span>
  </div>
  <div class="abs feature" style="left:450px">
    <div class="ico" style="background:var(--orange)">
      <svg width="40" height="40" viewBox="0 0 40 40"><g fill="#fff"><circle cx="20" cy="20" r="12"/><rect x="17" y="3" width="6" height="34" rx="1"/><rect x="3" y="17" width="34" height="6" rx="1"/><rect x="17" y="3" width="6" height="34" rx="1" transform="rotate(45 20 20)"/><rect x="17" y="3" width="6" height="34" rx="1" transform="rotate(-45 20 20)"/></g><circle cx="20" cy="20" r="5" fill="var(--orange)"/></svg>
    </div>
    <h3>What we offer</h3><div class="rule" style="background:var(--orange)"></div>
    <p>It is a long established fact that a reader be distracted by the readable content a page when looking at its layout. The point of using Lorem Ipsum of the round by</p>
    <span class="more">READ MORE</span>
  </div>
  <div class="abs feature" style="left:776px">
    <div class="ico" style="background:var(--green)">
      <svg width="40" height="40" viewBox="0 0 40 40"><rect x="16" y="2" width="8" height="36" fill="#fff"/><rect x="2" y="16" width="36" height="8" fill="#fff"/></svg>
    </div>
    <h3>Why Us</h3><div class="rule" style="background:var(--green)"></div>
    <p>It is a long established fact that a reader be distracted by the readable content a page when looking at its layout. The point of using Lorem Ipsum of the round by</p>
    <span class="more">READ MORE</span>
  </div>
</section>

<section class="about">
  <h2 class="abs section-title" style="top:68px">About Our Services</h2>
  <div class="abs title-rule" style="top:110px"></div>
  <div class="abs portrait" role="img" aria-label="Black and white portrait photo of the company founder"></div>
  <div class="abs person">
    <h4>Mara Elston</h4>
    <p>Lorem Ipsum is simply dummy text of the and typesetting industry. Lorem has been industry's dummy text ever since the when an unknown printer took a galley of type and scrambled it just want to need to be confortable for the most pecefull. <em>READ MORE</em></p>
  </div>

  <div class="abs svc" style="left:500px;top:205px">
    <div class="abs ring"><svg width="30" height="30" viewBox="0 0 30 30" fill="none" stroke="#333" stroke-width="1.6"><path d="M6 24l4-10 10-8 4 4-8 10z"/><path d="M6 24l7-7"/><path d="M4 27h10"/></svg></div>
    <h5 class="abs">Design</h5>
    <p class="abs">Focusing on the needs of users, applying science and new technologies, we design with detail modern spaces</p>
  </div>
  <div class="abs svc" style="left:828px;top:205px">
    <div class="abs ring hot"><svg width="34" height="34" viewBox="0 0 34 34" stroke="#fff" stroke-width="3.5" stroke-linecap="round"><path d="M7 27L27 7"/><path d="M7 7l20 20"/><path d="M4 10l6-6"/><path d="M24 4l6 6"/></svg></div>
    <h5 class="abs">Build</h5>
    <p class="abs">Focusing on the needs of users, applying science and new technologies, we design with detail modern spaces</p>
  </div>
  <div class="abs svc" style="left:500px;top:351px">
    <div class="abs ring"><svg width="34" height="22" viewBox="0 0 34 22" fill="none" stroke="#333" stroke-width="1.8"><rect x="2" y="3" width="27" height="16" rx="3"/><rect x="30" y="8" width="3" height="6" fill="#333"/><path d="M17 6l-5 6h6l-4 5" stroke-width="1.5"/></svg></div>
    <h5 class="abs">Operate</h5>
    <p class="abs">Focusing on the needs of users, applying science and new technologies, we design with detail modern spaces</p>
  </div>
  <div class="abs svc" style="left:828px;top:351px">
    <div class="abs ring"><svg width="34" height="32" viewBox="0 0 34 32"><path d="M17 2C9 2 3 7 3 14c0 4 2 7 5 9l-2 7 8-5c1 0 2 .1 3 .1 8 0 14-5 14-11S25 2 17 2z" fill="#111"/><text x="17" y="20" fill="#fff" font-size="14" font-weight="700" text-anchor="middle" font-family="Open Sans,sans-serif">?</text></svg></div>
    <h5 class="abs">Consulting</h5>
    <p class="abs">Focusing on the needs of users, applying science and new technologies, we design with detail modern spaces</p>
  </div>
</section>

<section class="gallery">
  <div class="abs tabs"><span class="on">PROJECT GALLERY</span><span>SET PROJECT GALLERY</span></div>
  <div class="abs tile" style="left:0;top:98px;background:linear-gradient(#3a5680,#25406a)" role="img" aria-label="Photo of cranes over a building site"><span class="view">View Details</span></div>
  <div class="abs tile" style="left:300px;top:98px;background:linear-gradient(135deg,#4d5a4a,#2e3a3a)" role="img" aria-label="Aerial photo of a highway interchange"><b>Project Title Goes Here</b><small>▦ April 06 | 9:00AM</small></div>
  <div class="abs tile" style="left:600px;top:98px;background:linear-gradient(135deg,#3f6b7a,#1f3d4c)" role="img" aria-label="Photo of a modern curved building by the water"><b>Project Title Goes Here</b><small>▦ April 06 | 9:00AM</small></div>
  <div class="abs tile" style="left:900px;top:98px;background:linear-gradient(135deg,#8a8a86,#5d5e5c)" role="img" aria-label="Architectural plan drawing"><b>Project Title Goes Here</b><small>▦ April 06 | 9:00AM</small></div>
  <div class="abs tile" style="left:0;top:297px;background:linear-gradient(135deg,#5b4d44,#3a302c)" role="img" aria-label="Photo of workers laying rebar"><b>Project Title Goes Here</b><small>▦ April 06 | 9:00AM</small></div>
  <div class="abs tile" style="left:300px;top:297px;background:linear-gradient(135deg,#4c5058,#2e3038)" role="img" aria-label="Photo of a city skyline"><b>Project Title Goes Here</b><small>▦ April 06 | 9:00AM</small></div>
  <div class="abs tile" style="left:600px;top:297px;background:linear-gradient(135deg,#2e3d55,#1a2538)" role="img" aria-label="Night photo of a modern building complex"><b>Project Title Goes Here</b><small>▦ April 06 | 9:00AM</small></div>
  <div class="abs tile" style="left:900px;top:297px;background:linear-gradient(135deg,#5e6a78,#3e4652)" role="img" aria-label="Photo of a team reviewing an architectural model"><b>Project Title Goes Here</b><small>▦ April 06 | 9:00AM</small></div>
</section>

<section class="news">
  <h2 class="abs section-title" style="top:84px">Our Latest News</h2>
  <div class="abs title-rule" style="top:125px"></div>
  <article class="abs item" style="left:110px;top:160px">
    <div class="abs pic" style="background:linear-gradient(135deg,#6b5a4a,#2d2a2a)" role="img" aria-label="Photo of an audience at a conference"></div>
    <h6 class="abs">Title Goes Here</h6>
    <p class="abs">Lorem Ipsum is simply dummy text of the printing and typesetting industry. Lorem Ipsum <em>Read More..</em></p>
    <span class="abs date">AUG 5, 2015</span>
  </article>
  <article class="abs item" style="left:667px;top:160px">
    <div class="abs pic" style="background:linear-gradient(135deg,#7a8a5a,#3a3e2e)" role="img" aria-label="Photo of site workers in safety vests"></div>
    <h6 class="abs">Title Goes Here</h6>
    <p class="abs">Lorem Ipsum is simply dummy text of the printing and typesetting industry. Lorem Ipsum <em>Read More..</em></p>
    <span class="abs date">AUG 5, 2015</span>
  </article>
  <article class="abs item" style="left:110px;top:343px">
    <div class="abs pic" style="background:linear-gradient(135deg,#b8a860,#5e6a4a)" role="img" aria-label="Photo of an award ceremony"></div>
    <h6 class="abs">Title Goes Here</h6>
    <p class="abs">Lorem Ipsum is simply dummy text of the printing and typesetting industry. Lorem Ipsum <em>Read More..</em></p>
    <span class="abs date">AUG 5, 2015</span>
  </article>
  <article class="abs item" style="left:667px;top:343px">
    <div class="abs pic" style="background:linear-gradient(135deg,#8fb6e0,#2f5a9a)" role="img" aria-label="Photo of engineers in hard hats reviewing plans"></div>
    <h6 class="abs">Title Goes Here</h6>
    <p class="abs">Lorem Ipsum is simply dummy text of the printing and typesetting industry. Lorem Ipsum <em>Read More..</em></p>
    <span class="abs date">AUG 5, 2015</span>
  </article>
</section>

<section class="cta" role="img" aria-label="Blue-toned photo of workers silhouetted on a construction site">
  <h2 class="abs">READY TO TALK ABOUT YOUR NEXT PROJECT?</h2>
  <div class="abs btn">Contact Us Now</div>
</section>

<footer class="site-footer">
  <div class="abs col" style="left:110px">
    <h4>INFO</h4>
    <ul><li>Home</li><li>Profile</li><li>Services</li><li>Works</li><li>Contact</li></ul>
  </div>
  <div class="abs col" style="left:359px">
    <h4>ABOUT US</h4>
    <p>There are many variations of passages of Lorem Ipsum available, but the majority have suffered alteration in some form, by injected humour, or randomised words which don't look even slightly believable.</p>
  </div>
  <div class="abs col" style="left:617px">
    <h4>CONTACT US</h4>
    <div class="contact-line"><svg width="10" height="13" viewBox="0 0 10 13"><path d="M5 0a5 5 0 0 0-5 5c0 4 5 8 5 8s5-4 5-8a5 5 0 0 0-5-5z" fill="#ccc"/><circle cx="5" cy="5" r="2" fill="#222528"/></svg><span>18 Harbor Lane<br>Westfield Park<br>Unit 7B</span></div>
    <div class="contact-line"><svg width="11" height="10" viewBox="0 0 11 10"><path d="M1 3c2-3 7-3 9 0v2H8V4H3v1H1z" fill="#ccc"/><rect x="2" y="6" width="7" height="4" fill="#ccc"/></svg><span>555.014.2290</span></div>
    <div class="contact-line"><svg width="11" height="9" viewBox="0 0 11 9"><rect width="11" height="9" fill="#ccc"/><path d="M0 0l5.5 5L11 0" stroke="#222528" fill="none"/></svg><span>hello@stratobuild.com</span></div>
  </div>
  <div class="abs col" style="left:871px;width:218px">
    <h4>NEWSLETTER SIGN UP</h4>
    <div class="field"></div>
    <div class="btn sub">SUBSCRIBE</div>
  </div>
  <div class="abs bottom">
    <div class="abs copy">© Copyright 2014 Stratobuild Engineers. All Rights Reserved - <b>Privacy Policy</b></div>
    <div class="abs follow">Follow Us : <i></i>|<i></i>|<i></i>|<i></i></div>
  </div>
</footer>

</body>
</html>
```